Redesign Power Point Template

we would like to update our powerpoint template. The current design limits the available space. we would like to keep the same colors and logo but have more room for content. We need both standard and cover template. I have attached our current template. we do not want to include the tag line "change your perspective" or the graph.

```html
<!DOCTYPE html>
<html lang="en">
<head>
<meta charset="utf-8">
<title>Corvana Presentation Template</title>
<link rel="stylesheet" href="https://fonts.googleapis.com/css2?family=Open+Sans:wght@400;600;700;800&display=swap">
<style>
  :root {
    --stage: #6b696b;
    --paper: #ffffff;
    --green: #4f9a3c;
    --ink: #111111;
    --muted: #9a9a9a;
    --subtitle: #666666;
    --rule: #c8c8c8;
    --band: #efefef;
    --photo-a: #b06a10;
    --photo-b: #2d6fa8;
  }
  * { box-sizing: border-box; margin: 0; padding: 0; }
  html, body { width: 1200px; height: 988px; overflow: hidden; }
  body { background: var(--stage); font-family: "Open Sans", sans-serif; position: relative; }

  .slide { position: absolute; width: 562px; height: 305px; background: var(--paper); overflow: hidden; }
  .slide--a { left: 23px; } .slide--b { left: 617px; }
  .row-1 { top: 18px; } .row-2 { top: 341px; } .row-3 { top: 664px; }

  .brand { position: absolute; display: flex; align-items: center; gap: 4px; color: var(--ink); font-weight: 800; letter-spacing: -0.5px; line-height: 1; white-space: nowrap; }
  .brand__mark { background: var(--green); display: block; flex: none; }
  .brand--corner { right: 20px; top: 17px; font-size: 19px; }
  .brand--corner .brand__mark { width: 10px; height: 10px; }

  .rule { position: absolute; width: 1px; background: var(--rule); }
  .accent { position: absolute; width: 4px; background: var(--green); }

  .subtitle { position: absolute; font-size: 13.5px; color: var(--subtitle); line-height: 1; }
  .para-title { position: absolute; font-size: 17px; font-weight: 700; color: var(--green); line-height: 1; }
  .body-copy { position: absolute; font-size: 7.1px; line-height: 14.5px; color: var(--muted); }
  .body-copy p + p { margin-top: 14.5px; }

  .footer { position: absolute; left: 0; right: 0; bottom: 0; height: 16px; background: var(--band); font-size: 8px; color: #333; padding: 3px 8px; }
  .page-num { position: absolute; right: 6px; bottom: 4px; width: 18px; height: 18px; border-radius: 50%; background: var(--green); color: #fff; font-size: 7.5px; font-weight: 700; display: flex; align-items: center; justify-content: center; }

  /* cover */
  .cover__graphic { position: absolute; left: 0; top: 0; width: 332px; height: 305px; background: linear-gradient(160deg, #000 0%, #111 45%, var(--green) 46%, var(--green) 100%); clip-path: ellipse(100% 130% at 0% 100%); }
  .cover__brand { left: 318px; top: 122px; font-size: 42px; }
  .cover__brand .brand__mark { width: 18px; height: 18px; }
  .cover__title { position: absolute; left: 355px; top: 224px; font-size: 20px; font-weight: 700; color: var(--green); }
  .cover__sub { position: absolute; left: 356px; top: 251px; font-size: 15px; color: var(--ink); }

  .feature-brand { left: 22px; top: 132px; font-size: 36px; }
  .feature-brand .brand__mark { width: 16px; height: 16px; }

  .photo { position: absolute; left: 0; top: 42px; width: 244px; height: 218px; background: radial-gradient(ellipse at 35% 30%, var(--photo-a) 0%, #e0b56a 35%, #fff 70%), linear-gradient(90deg, var(--photo-b), #fff); background-blend-mode: multiply; }

  .icon-item { position: absolute; top: 105px; width: 140px; text-align: center; }
  .icon-item svg { display: block; margin: 0 auto; height: 46px; }
  .icon-item h3 { font-size: 10px; font-weight: 700; color: var(--green); margin-top: 14px; line-height: 1; }
  .icon-item h3.dark { color: #555; }
  .icon-item p { font-size: 7.1px; line-height: 14.5px; color: var(--muted); margin-top: 4px; }
</style>
</head>
<body>

<!-- Cover -->
<section class="slide slide--a row-1">
  <div class="cover__graphic" role="img" aria-label="Large green and black segmented brand decoration"></div>
  <div class="brand cover__brand"><span class="brand__mark"></span>Corvana</div>
  <div class="rule" style="left:344px; top:204px; height:101px;"></div>
  <div class="accent" style="left:342px; top:218px; height:47px;"></div>
  <h1 class="cover__title">Project Title Here</h1>
  <p class="cover__sub">Subtitle Here</p>
</section>

<!-- Full-width text -->
<section class="slide slide--b row-1">
  <div class="rule" style="left:29px; top:0; height:109px;"></div>
  <div class="accent" style="left:27px; top:49px; height:39px;"></div>
  <p class="subtitle" style="left:43px; top:45px;">Subtitle Here</p>
  <h2 class="para-title" style="left:43px; top:62px;">Paragraph Title</h2>
  <div class="brand brand--corner"><span class="brand__mark"></span>Corvana</div>
  <div class="body-copy" style="left:43px; top:88px; width:488px;">
    <p>Lorem Ipsum is simply dummy text of the printing and typesetting industry. Lorem Ipsum has been the industry's standard dummy text ever since the 1500s, when an unknown printer took a galley of type and scrambled it to make a type specimen book. It has survived not only five centuries, but also the leap into electronic typesetting, remaining essentially unchanged. It was popularised in the 1960s with the release of Letraset sheets containing Lorem Ipsum passages, and more recently with desktop publishing software like Aldus PageMaker including versions of Lorem Ipsum. Lorem Ipsum is simply dummy text of the printing and typesetting industry.</p>
    <p>Lorem Ipsum has been the industry's standard dummy text ever since the 1500s, when an unknown printer took a galley of type and scrambled it to make a type specimen book. It has survived not only five centuries, but also the leap into electronic typesetting, remaining essentially unchanged.</p>
    <p>It was popularised in the 1960s with the release of Letraset sheets containing Lorem Ipsum passages, and more recently with desktop publishing software like Aldus PageMaker including versions of Lorem Ipsum.</p>
  </div>
  <footer class="footer">Copyright text here</footer>
  <span class="page-num">01</span>
</section>

<!-- Brand + text -->
<section class="slide slide--a row-2">
  <div class="brand feature-brand"><span class="brand__mark"></span>Corvana</div>
  <div class="rule" style="left:248px; top:0; height:269px;"></div>
  <div class="accent" style="left:246px; top:80px; height:39px;"></div>
  <p class="subtitle" style="left:262px; top:88px;">Subtitle Here</p>
  <h2 class="para-title" style="left:262px; top:105px;">Paragraph Title</h2>
  <div class="body-copy" style="left:262px; top:129px; width:268px;">
    <p>Lorem Ipsum is simply dummy text of the printing and typesetting industry. Lorem Ipsum has been the industry's standard dummy text ever since the 1500s, when an unknown printer took a galley of type and scrambled it to make a type specimen book. It has survived not only five centuries, but also the leap into electronic typesetting, remaining essentially unchanged. It was popularised in the 1960s with the release of Letraset sheets containing Lorem Ipsum passages, and more recently with desktop publishing software like Aldus PageMaker including versions of Lorem Ipsum.</p>
  </div>
  <footer class="footer">Copyright text here</footer>
  <span class="page-num">01</span>
</section>

<!-- Two columns -->
<section class="slide slide--b row-2">
  <div class="rule" style="left:29px; top:0; height:109px;"></div>
  <div class="accent" style="left:27px; top:31px; height:39px;"></div>
  <p class="subtitle" style="left:43px; top:35px;">Subtitle Here</p>
  <h2 class="para-title" style="left:43px; top:52px;">Paragraph Title</h2>
  <div class="brand brand--corner" style="right:13px;"><span class="brand__mark"></span>Corvana</div>
  <div class="body-copy" style="left:43px; top:75px; width:228px;">
    <p>Lorem Ipsum is simply dummy text of the printing and typesetting industry. Lorem Ipsum has been the industry's standard dummy text ever since the 1500s, when an unknown printer took a galley of type and scrambled it to make a type specimen book. It has survived not only five centuries, but also the leap into electronic typesetting, remaining essentially unchanged. It was popularised in the 1960s with the release of Letraset sheets containing Lorem Ipsum passages, and more recently with desktop publishing software like Aldus PageMaker including versions of Lorem Ipsum. Lorem Ipsum is simply dummy text of the printing and typesetting industry. Lorem Ipsum has been the industry's</p>
  </div>
  <div class="body-copy" style="left:301px; top:75px; width:228px;">
    <p>Lorem Ipsum is simply dummy text of the printing and typesetting industry. Lorem Ipsum has been the industry's standard dummy text ever since the 1500s, when an unknown printer took a galley of type and scrambled it to make a type specimen book. It has survived not only five centuries, but also the leap into electronic typesetting, remaining essentially unchanged. It was popularised in the 1960s with the release of Letraset sheets containing Lorem Ipsum passages, and more recently with desktop publishing software like Aldus PageMaker including versions of Lorem Ipsum. Lorem Ipsum is simply dummy text of the printing and typesetting industry. Lorem Ipsum has been the industry's</p>
  </div>
  <footer class="footer">Copyright text here</footer>
  <span class="page-num">01</span>
</section>

<!-- Image + text -->
<section class="slide slide--a row-3">
  <div class="photo" role="img" aria-label="Photo of an amber pill bottle spilling colourful capsules"></div>
  <div class="brand brand--corner" style="right:12px; top:13px;"><span class="brand__mark"></span>Corvana</div>
  <div class="rule" style="left:248px; top:0; height:269px;"></div>
  <div class="accent" style="left:246px; top:80px; height:39px;"></div>
  <p class="subtitle" style="left:262px; top:88px;">Subtitle Here</p>
  <h2 class="para-title" style="left:262px; top:105px;">Paragraph Title</h2>
  <div class="body-copy" style="left:262px; top:129px; width:268px;">
    <p>Lorem Ipsum is simply dummy text of the printing and typesetting industry. Lorem Ipsum has been the industry's standard dummy text ever since the 1500s, when an unknown printer took a galley of type and scrambled it to make a type specimen book. It has survived not only five centuries, but also the leap into electronic typesetting, remaining essentially unchanged. It was popularised in the 1960s with the release of Letraset sheets containing Lorem Ipsum passages, and more recently with desktop publishing software like Aldus PageMaker including versions of Lorem Ipsum.</p>
  </div>
  <footer class="footer">Copyright text here</footer>
  <span class="page-num">01</span>
</section>

<!-- Icons -->
<section class="slide slide--b row-3">
  <div class="rule" style="left:29px; top:0; height:109px;"></div>
  <div class="accent" style="left:27px; top:31px; height:39px;"></div>
  <p class="subtitle" style="left:43px; top:35px;">Subtitle Here</p>
  <h2 class="para-title" style="left:43px; top:52px;">Paragraph Title</h2>
  <div class="brand brand--corner" style="right:13px;"><span class="brand__mark"></span>Corvana</div>

  <div class="icon-item" style="left:56px;">
    <svg viewBox="0 0 46 46" aria-hidden="true">
      <rect x="15" y="2" width="20" height="40" rx="3" fill="none" stroke="var(--green)" stroke-width="3"/>
      <path d="M4 26 q0 -10 12 -12 v22 q-12 0 -12 -10z" fill="var(--green)"/>
      <rect x="30" y="18" width="7" height="4" rx="2" fill="var(--green)"/>
      <rect x="30" y="24" width="7" height="4" rx="2" fill="var(--green)"/>
      <rect x="30" y="30" width="7" height="4" rx="2" fill="var(--green)"/>
    </svg>
    <h3>Icon Text Here</h3>
    <p>Lorem Ipsum is simply dummy text of the printing and typesetting industry. Lorem Ipsum has been the industry's standard dummy text ever since the 1500s, when an unknown printer took a galley of type and scrambled</p>
  </div>

  <div class="icon-item" style="left:226px;">
    <svg viewBox="0 0 52 46" aria-hidden="true" fill="#8a8a8a">
      <circle cx="26" cy="9" r="6"/><path d="M17 40 v-17 q0 -7 9 -7 q9 0 9 7 v17z"/>
      <circle cx="12" cy="15" r="5"/><path d="M4 40 v-13 q0 -6 8 -6 q4 0 5 2 v17z"/>
      <circle cx="40" cy="15" r="5"/><path d="M48 40 v-13 q0 -6 -8 -6 q-4 0 -5 2 v17z"/>
    </svg>
    <h3 class="dark">Icon Text Here</h3>
    <p>Lorem Ipsum is simply dummy text of the printing and typesetting industry. Lorem Ipsum has been the industry's standard dummy text ever since the 1500s, when an unknown printer took a galley of type and scrambled</p>
  </div>

  <div class="icon-item" style="left:401px;">
    <svg viewBox="0 0 46 46" aria-hidden="true" fill="none" stroke="var(--green)" stroke-width="1.6">
      <rect x="5" y="30" width="5" height="14"/><rect x="13" y="24" width="5" height="20"/>
      <rect x="21" y="20" width="5" height="24"/><rect x="29" y="14" width="5" height="30"/>
      <rect x="37" y="8" width="5" height="36"/>
      <polyline points="6,22 15,16 23,13 31,7 40,2"/>
    </svg>
    <h3>Icon Text Here</h3>
    <p>Lorem Ipsum is simply dummy text of the printing and typesetting industry. Lorem Ipsum has been the industry's standard dummy text ever since the 1500s, when an unknown printer took a galley of type and scrambled</p>
  </div>

  <footer class="footer">Copyright text here</footer>
  <span class="page-num">01</span>
</section>

</body>
</html>
```